Post Card Design Bright Lantern Youth

We need a postcard design that will be mailed to all residents offering free pickups of donated clothing. Our foundation is called Bright Lantern Youth, we are a nonprofit charitable organization that provides meals and medical services to children in need in Honduras. Collecting unwanted second-hand clothing generates revenue that helps fund the mission and programs run by our foundation. We would like to offer our pickup services to everyone who has any unwanted reusable clothing.

```html
<!DOCTYPE html>
<html lang="en">
<head>
<meta charset="utf-8">
<title>Bright Lantern Youth – Clothing Donation Postcard</title>
<link rel="stylesheet" href="https://fonts.googleapis.com/css2?family=Poppins:wght@600;700&family=Roboto:wght@400;500;700&family=Roboto+Condensed:ital,wght@0,500;1,500&display=swap">
<style>
  :root {
    --page-bg: #ecebe7;
    --brand-green: #7cc242;
    --bar-green: #7dbb3c;
    --magenta: #e3127f;
    --sky-blue: #1790d6;
    --deep-blue: #0b6fb8;
    --pale-blue: #dff1fb;
    --sun-yellow: #f2c316;
    --text-yellow: #f7e51c;
    --ink: #111111;
    --stamp-grey: #dedfe0;
    --white: #ffffff;
    --alert-red: #e2192a;
  }
  * { margin: 0; padding: 0; box-sizing: border-box; }
  html, body { width: 1200px; height: 900px; overflow: hidden; }
  body { background: var(--page-bg); font-family: "Roboto", Arial, sans-serif; position: relative; }

  .postcard {
    position: absolute; left: 290px; width: 620px; height: 413px;
    overflow: hidden; background: var(--white);
    box-shadow: 0 2px 6px rgba(0,0,0,0.18);
  }
  .postcard--back { top: 30px; }
  .postcard--front { top: 457px; }
  .postcard svg.shapes { position: absolute; inset: 0; }

  /* Back side */
  .info-panel {
    position: absolute; left: 0; top: 0; width: 362px; height: 413px;
    background: linear-gradient(180deg, var(--pale-blue) 0%, #f3fafd 70%);
  }
  .brand-name {
    font-family: "Poppins", Arial, sans-serif; font-weight: 600;
    color: var(--brand-green); white-space: nowrap;
  }
  .info-panel .brand-name {
    position: absolute; top: 110px; left: 0; width: 362px; text-align: center; font-size: 30px;
  }
  .mission-text {
    position: absolute; left: 74px; top: 186px; width: 232px;
    font-size: 11.4px; line-height: 1.26; font-weight: 500; color: var(--ink);
  }
  .mission-text strong { font-size: 13px; font-weight: 500; }
  .back-call {
    position: absolute; left: 0; width: 362px; top: 342px; text-align: center;
    font-family: "Roboto Condensed", Arial, sans-serif; font-weight: 500;
    font-size: 14.5px; color: var(--white);
  }
  .back-phone {
    position: absolute; left: 60px; top: 364px;
    font-family: "Roboto", Arial, sans-serif; font-weight: 700;
    font-size: 26px; color: var(--white); display: flex; align-items: center; gap: 4px;
  }
  .stamp-box {
    position: absolute; left: 527px; top: 9px; width: 87px; height: 87px;
    background: var(--stamp-grey); border: 2px dotted #f5f5f5;
  }

  /* Front side */
  .front-brand { position: absolute; top: 28px; left: 20px; width: 340px; text-align: center; font-size: 29px; }
  .headline {
    position: absolute; top: 68px; left: 20px; width: 340px; text-align: center;
    font-family: "Poppins", Arial, sans-serif; font-weight: 700;
    font-size: 76px; line-height: 1; color: var(--magenta); letter-spacing: -1px;
  }
  .subhead {
    position: absolute; top: 154px; left: 20px; width: 340px; text-align: center;
    font-family: "Roboto", Arial, sans-serif; font-weight: 700; font-size: 23px;
    color: var(--sky-blue);
  }
  .subhead .accent { color: var(--magenta); }
  .gift-message {
    position: absolute; left: 37px; top: 254px; width: 220px;
    font-weight: 700; font-size: 19.5px; line-height: 1.2; color: var(--white);
  }
  .gift-message .highlight { color: var(--text-yellow); }
  .pickup-badge {
    position: absolute; left: 250px; top: 193px; width: 130px; height: 130px; border-radius: 50%;
    background: var(--sun-yellow); border: 3px solid var(--white);
    display: flex; flex-direction: column; align-items: center; justify-content: center;
    font-weight: 700; color: var(--ink); line-height: 1.05;
  }
  .pickup-badge .badge-line { font-size: 18px; }
  .pickup-badge .badge-free {
    font-family: "Poppins", Arial, sans-serif; font-size: 35px; color: var(--alert-red); line-height: 1.05;
  }
  .front-call {
    position: absolute; left: 47px; top: 343px;
    font-family: "Roboto Condensed", Arial, sans-serif; font-style: italic; font-weight: 500;
    font-size: 14.5px; color: var(--ink);
  }
  .front-phone {
    position: absolute; left: 44px; top: 374px;
    font-weight: 700; font-size: 27px; color: var(--white);
    display: flex; align-items: center; gap: 4px;
  }
  .hero-illustration {
    position: absolute; left: 0; top: 0; width: 620px; height: 413px;
  }
  .corner-brand { position: absolute; right: 10px; bottom: 14px; font-size: 13px; }
</style>
</head>
<body>

<section class="postcard postcard--back" aria-label="Postcard back">
  <div class="info-panel">
    <svg class="shapes" width="362" height="413" viewBox="0 0 362 413">
      <path d="M0 360 C120 318 250 300 362 182 L362 413 L0 413 Z" fill="var(--brand-green)"/>
      <path d="M0 372 C125 330 255 312 362 196 L362 413 L0 413 Z" fill="var(--sky-blue)"/>
    </svg>
    <div class="brand-name">Bright Lantern Youth</div>
    <p class="mission-text"><strong>Bright Lantern Youth</strong> is a nonprofit organization providing meals and medical services to children in need across Honduras. Your gently used clothing can fund life-changing programs and provide hope to those who need it most.</p>
    <p class="back-call">Call us to schedule your pickup</p>
    <p class="back-phone">
      <svg width="18" height="22" viewBox="0 0 24 24" aria-hidden="true"><path fill="#fff" d="M6.6 10.8c1.4 2.8 3.8 5.1 6.6 6.6l2.2-2.2c.3-.3.7-.4 1-.2 1.1.4 2.3.6 3.6.6.6 0 1 .4 1 1V20c0 .6-.4 1-1 1C10.6 21 3 13.4 3 4c0-.6.4-1 1-1h3.5c.6 0 1 .4 1 1 0 1.3.2 2.5.6 3.6.1.3 0 .7-.2 1L6.6 10.8z"/></svg>
      1-555-014-2738
    </p>
  </div>
  <div class="stamp-box" aria-label="Stamp area"></div>
</section>

<section class="postcard postcard--front" aria-label="Postcard front">
  <div class="hero-illustration" role="img" aria-label="Illustration of a smiling child with a backpack among colourful leaves"
       style="background: linear-gradient(90deg, transparent 0%, transparent 62%, #f4e3a6 66%, #8fc9e8 72%, #6b3a22 80%, #a85a35 88%, #2a93d0 100%);"></div>
  <svg class="shapes" width="620" height="413" viewBox="0 0 620 413">
    <path d="M0 172 C90 215 190 235 270 232 C330 230 380 215 420 200 L420 413 L0 413 Z" fill="var(--deep-blue)"/>
    <path d="M0 184 C90 226 190 246 270 243 C330 241 380 226 420 212 L420 413 L0 413 Z" fill="var(--sky-blue)"/>
    <path d="M0 370 L395 370 L355 413 L0 413 Z" fill="var(--bar-green)"/>
    <path d="M620 288 L620 413 L505 413 C545 380 590 330 620 288 Z" fill="var(--white)"/>
  </svg>
  <div class="brand-name front-brand">Bright Lantern Youth</div>
  <h1 class="headline">Donate</h1>
  <p class="subhead"><span class="accent">Clothing-</span>Change Lives!</p>
  <p class="gift-message">Give the gift of care today <span class="highlight">your donation makes a difference!</span></p>
  <div class="pickup-badge">
    <span class="badge-line">We offer</span>
    <span class="badge-free">FREE</span>
    <span class="badge-line">pickups</span>
  </div>
  <p class="front-call">Call us to schedule your pickup</p>
  <p class="front-phone">
    <svg width="18" height="22" viewBox="0 0 24 24" aria-hidden="true"><path fill="#fff" d="M6.6 10.8c1.4 2.8 3.8 5.1 6.6 6.6l2.2-2.2c.3-.3.7-.4 1-.2 1.1.4 2.3.6 3.6.6.6 0 1 .4 1 1V20c0 .6-.4 1-1 1C10.6 21 3 13.4 3 4c0-.6.4-1 1-1h3.5c.6 0 1 .4 1 1 0 1.3.2 2.5.6 3.6.1.3 0 .7-.2 1L6.6 10.8z"/></svg>
    1-555-014-2738
  </p>
  <div class="brand-name corner-brand">Bright Lantern Youth</div>
</section>

</body>
</html>
```